Platelet Rich Plasma (PRP) Flyer

Hi,

Looking to spruce up our Platelet Rich Plasma Flyer (see power point attachment). I also included previous flyers as examples on the design style we are looking for.

Quorum is our official font of our logo.
Attached is our logo in EPS format.
Please use the current photos in the power point. If you include photos, please make sure the stock image is free.

Files must be under 5MB. JPEG, PNG, PDF, .ai

Thank you,
Dorian

Target Market(s)

Patients

Industry/Entity Type

Healthcare

Font styles to use
Other font styles liked:
• Quorum

Requirements
Must have
• Emphasis on Platelet Rich Plasma Therapy when they pick up the flyer. The price of $199. FSA/HSA Eligible. The different treatment areas. The three addresses. Best of the best logo can be very small, not as important.
Nice to have
• One or two pictures. Less is more
Should not have
• Long paragraphs, multiple sentences.

```html
<!DOCTYPE html>
<html lang="en">
<head>
<meta charset="UTF-8">
<title>Ridgeview Foot & Ankle – PRP Therapy Flyer</title>
<link href="https://fonts.googleapis.com/css2?family=Oswald:wght@500;600;700&family=Roboto:wght@400;500;700&display=swap" rel="stylesheet">
<style>
  :root{
    --ink:#2d2d2d;
    --orange:#e07548;
    --orange-light:#f08a58;
    --orange-text:#f07f4a;
    --teal:#55c3a5;
    --white:#ffffff;
    --photo-light:#bdbdbd;
    --photo-dark:#6f6f6f;
  }
  html,body{margin:0;padding:0;overflow:hidden;background:var(--ink);}
  .flyer{position:relative;width:927px;height:1200px;background:var(--ink);overflow:hidden;font-family:"Roboto",Arial,sans-serif;color:var(--white);}
  .hero-art{position:absolute;left:0;top:0;width:927px;height:575px;}
  .phone-tab{position:absolute;right:0;top:0;width:276px;height:52px;background:var(--teal);border-bottom-left-radius:52px;display:flex;align-items:center;justify-content:flex-end;padding-right:54px;box-sizing:border-box;gap:10px;}
  .phone-tab span{font-family:"Oswald",Arial,sans-serif;font-weight:500;font-size:23px;letter-spacing:.5px;color:var(--white);}
  .brand{position:absolute;left:54px;top:40px;display:flex;align-items:center;gap:12px;}
  .brand-dot{width:56px;height:56px;border-radius:50%;background:var(--teal);}
  .brand-name{font-family:"Oswald",Arial,sans-serif;font-weight:600;font-size:29px;line-height:30px;color:var(--orange-text);text-transform:uppercase;}
  .brand-web{display:block;font-size:13px;line-height:16px;letter-spacing:.3px;text-align:right;}
  .services{position:absolute;left:54px;top:202px;font-weight:700;font-size:16px;line-height:24px;margin:0;}
  .headline{position:absolute;left:54px;top:264px;font-weight:700;font-size:27px;line-height:38.5px;margin:0;}
  .price{position:absolute;left:53px;top:428px;font-family:"Oswald",Arial,sans-serif;font-weight:700;font-size:41px;line-height:46px;letter-spacing:1px;margin:0;}
  .price u{text-decoration-thickness:2px;text-underline-offset:3px;}
  .eligible{position:absolute;left:54px;top:532px;font-weight:700;font-size:16px;line-height:20px;letter-spacing:.5px;margin:0;}
  .section-title{position:absolute;left:0;width:927px;text-align:center;font-family:"Oswald",Arial,sans-serif;font-weight:600;color:var(--teal);margin:0;letter-spacing:-.5px;}
  .prp-title{top:618px;font-size:35px;line-height:41px;}
  .treat-title{top:895px;font-size:35px;line-height:41px;}
  .title-bar{position:absolute;left:444px;width:40px;height:3px;background:var(--orange-text);}
  .intro{position:absolute;left:83px;width:761px;top:736px;text-align:center;font-size:16px;line-height:24px;font-weight:500;margin:0;}
  .intro p{margin:0 0 12px;}
  .conditions{position:absolute;left:0;width:927px;top:960px;text-align:center;font-size:24px;color:var(--orange-text);margin:0;}
  .office{position:absolute;top:1049px;width:232px;height:112px;background:var(--teal);border-radius:7px;box-sizing:border-box;padding:30px 24px 0;}
  .office .pin{position:absolute;left:20px;top:-20px;width:36px;height:36px;border-radius:50%;background:var(--ink);display:flex;align-items:center;justify-content:center;}
  .office .pin i{width:26px;height:26px;border-radius:50%;background:var(--white);display:flex;align-items:center;justify-content:center;}
  .office h3{margin:0 0 10px;font-size:14.5px;font-weight:700;text-decoration:underline;text-underline-offset:2px;}
  .office p{margin:0;font-size:13px;line-height:17px;}
  .code{position:absolute;left:888px;top:1154px;font-size:7px;}
  .bottom-band{position:absolute;left:0;bottom:0;width:927px;height:7px;background:var(--orange);}
</style>
</head>
<body>
<main class="flyer">
  <svg class="hero-art" viewBox="0 0 927 575">
    <defs>
      <linearGradient id="photoTone" x1="0" y1="0" x2="1" y2="1">
        <stop offset="0" stop-color="var(--photo-dark)"/>
        <stop offset=".55" stop-color="var(--photo-light)"/>
        <stop offset="1" stop-color="#e4e4e4"/>
      </linearGradient>
    </defs>
    <path role="img" aria-label="Black and white photo of hands massaging a painful foot arch" d="M511,0 L927,0 L927,305 L835,392 L740,571 L420,571 L357,159 Z" fill="url(#photoTone)"/>
    <path d="M0,158 H373 A206.5 206.5 0 0 1 578 364.5 A206.5 206.5 0 0 1 373 571 H0 Z" fill="var(--orange)"/>
    <circle cx="440" cy="364" r="138" fill="var(--orange-light)" opacity=".75"/>
    <circle cx="768" cy="471" r="96" fill="var(--ink)"/>
    <circle role="img" aria-label="Gloved hands placing blood tubes into a centrifuge" cx="772" cy="471" r="90" fill="url(#photoTone)"/>
  </svg>

  <div class="phone-tab">
    <svg width="18" height="18" viewBox="0 0 18 18"><rect width="18" height="18" rx="3" fill="var(--orange-text)"/><path d="M5 4c1 0 1.5 2 1.5 2.5S5.5 7.5 6 8.5s2 2.5 3.5 3 1-1 1.5-1 2.5.5 2.5 1.5-1 2-2 2C7 14 4 11 4 6c0-1 .5-2 1-2z" fill="var(--white)"/></svg>
    <span>(877) 555 - 0142</span>
  </div>

  <div class="brand">
    <div class="brand-dot"></div>
    <div class="brand-name">Ridgeview<br>Foot &amp; Ankle<span class="brand-web">stridewellfeet.com</span></div>
  </div>

  <p class="services">PODIATRY | FOOT &amp; ANKLE SURGERY SPORTS<br>MEDICINE | WOUND CARE</p>
  <p class="headline">SAME DAY | EMERGENCY |<br>SATURDAY APPOINTMENTS<br>OUR DOCTORS ARE ON CALL AT<br>THE RVH ER 24/7</p>
  <p class="price">SELF PAY PRICE:<br><u>$199 PER TREATMENT</u></p>
  <p class="eligible">FSA/HSA ELIGIBLE</p>

  <h1 class="section-title prp-title">PLATELET RICH<br>PLASMA THERAPY (PRP)</h1>
  <div class="title-bar" style="top:706px"></div>

  <div class="intro">
    <p>PRP uses the platelets in your own blood to speed tissue repair and healing.</p>
    <p>A consultation is required to make sure you qualify.</p>
  </div>

  <h2 class="section-title treat-title">TREATING</h2>
  <div class="title-bar" style="top:941px"></div>
  <p class="conditions">Plantar Fasciitis | Achilles Tendonitis | Tendon &amp; Ligament Injuries</p>

  <section class="office" style="left:80px">
    <span class="pin"><i><svg width="10" height="13" viewBox="0 0 10 13"><path d="M5 0a5 5 0 0 1 5 5c0 3.5-5 8-5 8S0 8.5 0 5a5 5 0 0 1 5-5z" fill="var(--orange-text)"/><circle cx="5" cy="5" r="1.8" fill="var(--white)"/></svg></i></span>
    <h3>WESTBROOK OFFICE</h3>
    <p>210 Cedar Point Dr. Ste. 140<br>Westbrook, MD 21790</p>
  </section>
  <section class="office" style="left:347px">
    <span class="pin"><i><svg width="10" height="13" viewBox="0 0 10 13"><path d="M5 0a5 5 0 0 1 5 5c0 3.5-5 8-5 8S0 8.5 0 5a5 5 0 0 1 5-5z" fill="var(--orange-text)"/><circle cx="5" cy="5" r="1.8" fill="var(--white)"/></svg></i></span>
    <h3>MILLBROOK OFFICE</h3>
    <p>5120 Harbor Crest Blvd. Ste.<br>305 Millbrook, MD 21795</p>
  </section>
  <section class="office" style="left:614px">
    <span class="pin"><i><svg width="10" height="13" viewBox="0 0 10 13"><path d="M5 0a5 5 0 0 1 5 5c0 3.5-5 8-5 8S0 8.5 0 5a5 5 0 0 1 5-5z" fill="var(--orange-text)"/><circle cx="5" cy="5" r="1.8" fill="var(--white)"/></svg></i></span>
    <h3>PINECREST OFFICE</h3>
    <p>88 Wellness Way Pinecrest,<br>WV 25490</p>
  </section>

  <span class="code">C45</span>
  <div class="bottom-band"></div>
</main>
</body>
</html>
```